Strong, Clean Book Design Needed for "The Lantern Keeper"

I need a strong, clean, masculine cover of a book that focuses on helping men restore honor to what it means to be a good husband. (I also need a back cover and spine done as well). I would like the cover to be either a white, red, or black cover. I have attached 3 books that I would like to use as examples to model after. I also attached a word document to show the potential layouts I would like to see and how that parallel the example covers.

Specs:
- Book is 150 pages long
- Size is 5.25 x 8

Target Market(s)

Christian men who are married or looking to be married.

Font styles to use
Serif
Sans Serif

Colors
ec1f27
f04a50
ffffff
000000
1b1b1b
757575

Requirements
Must have
• - A design that resembles/has a similar feel to one of the three examples that are attached and laid out similarly to one of the 3 designs in the word doc "3 Book Designs"
• - These elements on the front cover: Title: The Lantern Keeper, Subtitle: Restoring the honor of a Christ-centered marriage, Author Name: Dean Halvorsen
• - A strong design that is simple yet creative.
• - Strong masculine font that is bold but not too flashy
• - Red should be included either as the title font color or as the overall cover color.
• - The back of the book should have the attached file "Back of the book" text on the back
Nice to have
• - A color contrast, like a strip of another color (see "example 3" attached file) across the front for the subtitle or the author name.
• - Including the attached sword file as a somewhat transparent image on the cover, but absolutely not necessary.
• - If there is going to be any highlighting of words in the subtitle, they should be the word "honor" and "Christ-centered"
Should not have
• Any religious symbols, such as a cross.

```html
<!DOCTYPE html>
<html lang="en">
<head>
<meta charset="utf-8">
<title>The Lantern Keeper — Book Cover</title>
<link href="https://fonts.googleapis.com/css2?family=Alfa+Slab+One&family=Poppins:wght@300;400&display=swap" rel="stylesheet">
<style>
  :root {
    --red: #b4141b;
    --red-deep: #8e0d12;
    --red-light: #c92a2e;
    --ink: #0d0d0d;
    --paper: #ece6e6;
    --sub-ink: #2a2a2a;
    --placeholder: #cfcfcf;
    --placeholder-ink: #9a9a9a;
  }
  * { margin: 0; padding: 0; box-sizing: border-box; }
  html, body { width: 1200px; height: 893px; overflow: hidden; background: #fff; }
  .jacket {
    position: relative; width: 1200px; height: 893px; overflow: hidden;
    background:
      radial-gradient(ellipse at 30% 20%, rgba(255,255,255,0.06), transparent 55%),
      radial-gradient(ellipse at 80% 85%, rgba(0,0,0,0.22), transparent 60%),
      radial-gradient(ellipse at 10% 90%, rgba(0,0,0,0.2), transparent 50%),
      linear-gradient(180deg, var(--red-light), var(--red) 45%, var(--red-deep));
    font-family: 'Poppins', sans-serif;
  }
  .slab { font-family: 'Alfa Slab One', serif; text-align: center; position: absolute; line-height: 1; }

  /* Back cover */
  .back { position: absolute; left: 0; top: 0; width: 578px; height: 893px; }
  .back .t-the { top: 16px; left: 0; width: 578px; font-size: 22px; color: var(--ink); }
  .back .t-main { top: 46px; left: 0; width: 578px; font-size: 46px; color: var(--paper); }
  .back .t-sub { top: 100px; left: 0; width: 578px; font-size: 34px; color: var(--ink); }
  .blurb {
    position: absolute; left: 70px; top: 156px; width: 452px;
    color: #fff; font-size: 12.4px; line-height: 15.6px; text-align: justify; text-align-last: center;
  }
  .blurb p { margin-bottom: 15.6px; }
  .blurb .lead { text-align: center; }
  .rally {
    position: absolute; left: 70px; top: 592px; width: 460px;
    font-family: 'Alfa Slab One', serif; font-size: 14.4px; line-height: 20px; color: var(--ink);
  }
  .author-photo { position: absolute; left: 75px; top: 661px; }
  .bio {
    position: absolute; left: 216px; top: 668px; width: 307px;
    color: #fff; font-size: 12.2px; line-height: 15.6px; text-align: justify; text-align-last: left;
  }
  .barcode-slot {
    position: absolute; left: 346px; top: 811px; width: 176px; height: 71px;
    background: var(--placeholder); color: var(--placeholder-ink);
    font-size: 20px; line-height: 71px; text-align: center;
  }

  /* Spine */
  .spine { position: absolute; left: 578px; top: 0; width: 44px; height: 893px; background: var(--ink); }
  .spine-blade {
    position: absolute; left: 12px; top: 190px; width: 8px; height: 460px;
    background: linear-gradient(180deg, rgba(200,200,200,0.15), rgba(230,230,230,0.45), rgba(200,200,200,0.1));
  }
  .spine-text {
    position: absolute; left: 50%; writing-mode: vertical-rl;
    transform: translateX(-50%);
    font-family: 'Alfa Slab One', serif; font-size: 22px; color: #fff; white-space: nowrap; letter-spacing: 0.5px;
  }
  .spine-title { top: 24px; }
  .spine-author { top: 628px; }

  /* Front cover */
  .front { position: absolute; left: 622px; top: 0; width: 578px; height: 893px; }
  .front .t-the { top: 70px; left: 0; width: 578px; font-size: 44px; color: var(--ink); }
  .front .t-main {
    top: 176px; left: 0; width: 578px; font-size: 96px; color: var(--paper);
    background: linear-gradient(180deg, #f1ecec 60%, #bdb8b8); -webkit-background-clip: text; background-clip: text; -webkit-text-fill-color: transparent;
  }
  .front .sword-area {
    position: absolute; left: 18px; top: 252px; width: 556px; height: 48px;
    background: linear-gradient(90deg, rgba(40,20,20,0.75), rgba(150,20,25,0.7) 30%, rgba(170,160,160,0.55));
  }
  .front .t-sub { top: 336px; left: 0; width: 578px; font-size: 62px; color: var(--ink); }
  .strip { position: absolute; left: 0; top: 486px; }
  .subtitle {
    position: absolute; left: 0; top: 530px; width: 578px; text-align: center;
    font-weight: 300; font-size: 32px; line-height: 39px; color: var(--sub-ink); letter-spacing: 0.3px;
  }
  .front .author { top: 778px; left: 0; width: 578px; font-size: 44px; color: var(--paper); letter-spacing: 1px; }
</style>
</head>
<body>
<div class="jacket">

  <section class="back">
    <div class="slab t-the">THE</div>
    <div class="slab t-main">LANTERN</div>
    <div class="slab t-sub">KEEPER</div>

    <div class="blurb">
      <p class="lead">Do you have what it takes to be a Lantern Keeper?</p>
      <p>The samurai were fearsome Japanese warriors known for their discipline, loyalty, and strict adherence to their code of honor, bushido. Along with their ferocity on the battlefield, they also embodied the heart and sacrifice of “those who serve,” the meaning of the word samurai. The samurai lived, and more importantly, died by the honor that characterized these ideals. The samurai way of life transformed the nation, culture, and moral code of Japan, and continues to do so to this day…</p>
      <p>The Lantern Keeper is more than just an interesting read: it is a radically Christ-centered approach to marriage. Dean Halvorsen recaptures what it means to be a man and an effective leader in a marriage by simply, but powerfully, laying out the Biblical qualities found in Ephesians 5 that God calls husbands to embody. With a fresh and unique perspective, Dean parallels how samurai warriors once lived and how godly husbands should live in a way that restores and highlights the honor, sacrifice, and purpose of marriage. This book will undoubtedly shift the way men view and function in their role as a husband and gives them practical nuts and bolts suggestions for day-to-day success as a husband.</p>
      <p>This is a wake-up call to all husbands everywhere: be the man and the husband God has called you to be. Although it is not easy, it is guaranteed to transform your life… and your marriage!</p>
    </div>

    <div class="rally">Embrace the call of a truly Christ-centered marriage.<br>Embrace the way of the Lantern Keeper.</div>

    <svg class="author-photo" width="124" height="124" viewBox="0 0 124 124" role="img" aria-label="Author portrait">
      <circle cx="62" cy="62" r="62" fill="#000"/>
    </svg>

    <p class="bio">DEAN HALVORSEN is the Microchurch Pastor at the Cedar Hill Church in Asheville, North Carolina where he has a heart for marriage as well as multiplying disciples and churches. He has a fierce love for and has been married to his wife, Miriam, for over a decade. They have two beautiful daughters, Elise and Nora.</p>

    <div class="barcode-slot">BARCODE</div>
  </section>

  <section class="spine">
    <div class="spine-blade" role="img" aria-label="Faint sword running along the spine"></div>
    <div class="spine-text spine-title">THE LANTERN KEEPER</div>
    <div class="spine-text spine-author">DEAN HALVORSEN</div>
  </section>

  <section class="front">
    <div class="slab t-the">THE</div>
    <div class="slab t-main">LANTERN</div>
    <div class="sword-area" role="img" aria-label="Katana with a red ribbon laid across the title"></div>
    <div class="slab t-sub">KEEPER</div>

    <svg class="strip" width="578" height="190" viewBox="0 0 578 190" aria-hidden="true">
      <defs>
        <linearGradient id="steel" x1="0" y1="0" x2="0" y2="1">
          <stop offset="0" stop-color="#a9adb0"/>
          <stop offset="0.5" stop-color="#969a9d"/>
          <stop offset="1" stop-color="#7f8386"/>
        </linearGradient>
      </defs>
      <polygon fill="url(#steel)" points="0,30 90,24 190,28 260,18 330,22 420,10 500,14 578,6 578,130 500,140 410,150 330,146 250,162 170,158 90,176 0,182"/>
    </svg>
    <p class="subtitle">RESTORING THE HONOR OF A<br>CHRIST-CENTERED MARRIAGE</p>

    <div class="slab author">DEAN HALVORSEN</div>
  </section>

</div>
</body>
</html>
```